TALVEX PRINT CATALOGUE

Our company imports and distributes glass fencing products Australia wide. We need a new catalogue showcasing our products. Our target market is DIY customers, local and interstate. example at talvex.com.au
Industry/Entity Type
Fencing

```html
<!DOCTYPE html>
<html lang="en">
<head>
<meta charset="utf-8">
<title>Talvex – Instructions for Frameless Glass Installation</title>
<link rel="stylesheet" href="https://fonts.googleapis.com/css2?family=Exo+2:wght@400;600&family=Arimo:wght@700&display=swap">
<style>
  :root {
    --brand-blue: #13329a;
    --text-blue: #2a3f96;
    --footer-grey: #9a9a9a;
    --page-white: #ffffff;
    --photo-top: #7fa3c8;
    --photo-bottom: #b9ae9f;
  }
  * { margin: 0; padding: 0; box-sizing: border-box; }
  html, body { width: 1200px; height: 848px; overflow: hidden; background: var(--page-white); }
  .spread { position: relative; width: 1200px; height: 848px; font-family: "Exo 2", sans-serif; }

  .cover { position: absolute; left: 0; top: 0; width: 600px; height: 848px; }
  .cover-photo {
    position: absolute; inset: 0;
    background: linear-gradient(180deg, var(--photo-top) 0%, var(--photo-bottom) 100%);
  }
  .cover-title {
    position: absolute; left: 300px; top: 678px; width: 300px; height: 105px;
    background: var(--brand-blue); color: var(--page-white);
    font-family: "Arimo", sans-serif; font-weight: 700; padding: 20px 0 0 32px;
  }
  .cover-title .main { font-size: 22px; line-height: 26px; font-weight: 700; }
  .cover-title .sub { font-size: 15px; line-height: 20px; font-weight: 700; }

  .company-footer {
    position: absolute; top: 800px; width: 300px; text-align: center;
    font-size: 7.5px; line-height: 9.5px; color: var(--footer-grey);
  }
  .company-footer strong { font-weight: 600; }
  .company-footer.on-cover { left: 150px; color: #f3ece4; }
  .company-footer.on-page { left: 750px; }

  .step { position: absolute; left: 678px; width: 445px; color: var(--text-blue); }
  .step-heading { height: 25px; border-bottom: 2px solid var(--brand-blue); }
  .step-heading span {
    display: block; width: 253px; height: 24px; background: var(--brand-blue); color: var(--page-white);
    font-weight: 600; font-size: 13px; line-height: 24px; padding-left: 14px;
  }
  .step-body { margin-top: 8px; font-size: 11px; line-height: 13px; letter-spacing: 0.25px; }
  .step-body ol { list-style: none; counter-reset: item; }
  .step-body ol li { position: relative; padding-left: 17px; counter-increment: item; }
  .step-body ol li::before { content: counter(item) "."; position: absolute; left: 0; }
  .step-body ul { list-style: none; margin-top: 13px; }
  .step-body ul li { position: relative; padding-left: 17px; }
  .step-body ul li::before {
    content: ""; position: absolute; left: 0; top: 2px; width: 9px; height: 9px; background: var(--brand-blue);
  }
  .gap { margin-top: 13px; }
</style>
</head>
<body>
<div class="spread">
  <section class="cover">
    <div class="cover-photo" role="img" aria-label="Photo of a balcony with frameless glass fencing overlooking a river"></div>
    <div class="cover-title">
      <div class="main">INSTRUCTIONS</div>
      <div class="sub">FOR FRAMELESS GLASS<br>INSTALLATION</div>
    </div>
    <div class="company-footer on-cover">
      <strong>Talvex Holdings Pty Ltd</strong><br>
      48 Harbour Vale Drive, Marlowe Qld 4299<br>
      T: 1300 555 014 | F: (07) 5550 1827 | E: info@talvex.com.au
    </div>
  </section>

  <section class="step" style="top:35px;">
    <h2 class="step-heading"><span>Step 1 - Set out</span></h2>
    <div class="step-body">
      <p>The set out of your fence is the first and most important step to ensure the fence fits correctly.</p>
      <ol>
        <li>Firstly measure your area and draw your proposed plan on paper first.</li>
        <li>Mark the centreline of your fence on the concrete or timber surface.</li>
        <li>Stretch a chalk line between marks parallel with the outside edge of your slab or deck, generally we allow 100mm from edge to avoid chipping or breaking of edges when core drilling. 100mm in for edge will be you centreline of glass.</li>
        <li>Pull the chalk line tight and flick the line.</li>
        <li>Mark the panel lengths with a pencil over the chalk line and also mark the gaps between the panels.</li>
        <li>Place the spigots 150mm to centre in from the edge of panels.</li>
      </ol>
      <ul>
        <li>For Example - if a glass panel is 1000mm wide the spigot breakdown is 125mm in from the edge of the glass to the face of spigot. Leaving 650mm between the centres of the two spigots.</li>
        <li>NOTE: It is a good idea to check all measurements twice. All measurements should be with within a working tolerance of +/- 2mm.</li>
      </ul>
      <ol class="gap">
        <li>This position represents the centre of your core hole or the centre of your base plate spigot.</li>
        <li>Find the centre of the gate position and mark with a pencil. The gate opening for standard spring hinge gate is 850mm. Actual gate size being 834mm allowing 16mm for hinges and latch.</li>
        <li>You are now ready to core drill your holes or pilot hole for spigots fixed to decking.</li>
      </ol>
    </div>
  </section>

  <section class="step" style="top:415px;">
    <h2 class="step-heading"><span>Step 2 - Core Drilling</span></h2>
    <div class="step-body">
      <ol>
        <li>When your fence is to be fixed to a concrete substrate we recommend using a core drilled spigot to provide ultimate strength and ease of installation, providing a much stronger fixing than based mounted fixing and aesthetically more appealing.</li>
        <li>Using a core drill is pretty simple, simply select your size core bit, we recommend 75mm diameter core bit for square spigots and 65mm to suit round spigots. Read the instructions supplied from you local equipment hire provider before starting. A little trade tip is to use a piece of ply timber about 20mm thick. Make a guide hole through the timber using the core drill the same size. When you start each core hole use the guide to mark the holes and to start the hole to a depth of APR 10mm. Then remove the guide and start core drilling. REMEMBER always use water when core drilling.</li>
        <li>Drill a maximum of 200mm into concrete; generally 130mm - 180mm from top of tile to bottom of holes is perfect. DO NOT put too much downwards pressure on the core dill.</li>
        <li>Break the concrete core using a hammer and a large flat headed screw driver making sure you do not chip any pavers or tiles.</li>
        <li>Pull the concrete cores out of the hole. You may also need a small jack hammer to break away any concrete or reinforcing steel protruding into the finished core drill position.</li>
        <li>Wash away any concrete slurry; we have found a wet/dry vacuum works best to clean water and slurry from area.</li>
        <li>You are now ready to stand up your fence. The standard height panels are all 1200mm high so you know you will always comply.</li>
      </ol>
    </div>
  </section>

  <div class="company-footer on-page">
    <strong>Talvex Holdings Pty Ltd</strong><br>
    48 Harbour Vale Drive, Marlowe Qld 4299<br>
    T: 1300 555 014 | F: (07) 5550 1827 | E: info@talvex.com.au
  </div>
</div>
</body>
</html>
```